依頼詳細
上記のターゲットに郵送でDMを送り、注文がきたところに飛燕パックを利用して届けるのを考えています。
バナナ1ケース約2500円+運賃
メンバーが多いラグビー部は週4回、馬術部は1回みたいな感じです。
記載項目
社名や連絡先、URL、ロゴなど必要な情報は入れていただつつ、導入事例や注文者に記載していただく表(添付画像参照)なども入れていただきたく存じます。
サイズ
A4
ページ数
両面
希望イメージ
シンプル 複雑
単色 カラフル
暗い 明るい
日常 高級
遊び心 厳粛
未来的 伝統的
女性的 男性的
希望する色
黄 緑
納品ファイル
• 高解像度JPG (.jpg)
• イラストレーター形式 (.ai)

```html
<!DOCTYPE html>
<html lang="ja">
<head>
<meta charset="utf-8">
<title>バナナの宅配サービス</title>
<link rel="stylesheet" href="https://fonts.googleapis.com/css2?family=M+PLUS+Rounded+1c:wght@500;800;900&family=Noto+Sans+JP:wght@400;700&display=swap">
<style>
:root{
  --green:#3f9a2e;
  --green-dark:#2f7d22;
  --yellow-bg:#faf6c4;
  --yellow-band:#f5ee9a;
  --white:#ffffff;
  --ink:#333333;
  --line:#8bbf6e;
  --note:#f2c27a;
  --photo:#7d6a55;
}
*{margin:0;padding:0;box-sizing:border-box}
html,body{width:851px;height:1200px;overflow:hidden}
body{background:var(--white);font-family:"Noto Sans JP",sans-serif;color:var(--ink)}
.flyer{position:relative;width:851px;height:1200px;background:var(--yellow-bg)}
.abs{position:absolute}
.rounded{font-family:"M PLUS Rounded 1c",sans-serif}

.tagline{left:28px;top:18px;font-size:21px;font-weight:800;color:var(--green);display:flex;align-items:center;gap:8px}
.tagline .dot{width:18px;height:18px;border-radius:50%;background:var(--green)}
.title{left:28px;top:46px;font-size:60px;font-weight:900;color:var(--green);letter-spacing:1px}
.delivery-icon{right:34px;top:52px;width:70px;height:70px;border-radius:50%;background:var(--green)}

.price-band{left:28px;top:128px;width:795px;height:80px;display:flex}
.origin{width:270px;background:var(--green);color:var(--white);padding:10px 14px;display:flex;align-items:center;gap:12px}
.origin-name{font-size:25px;font-weight:800;line-height:1.15}
.brand{font-size:15px;font-weight:800;color:var(--white);display:flex;align-items:center;gap:4px}
.brand .sq{width:10px;height:10px;background:var(--white)}
.price{flex:1;background:var(--white);border:3px solid var(--green);display:flex;align-items:center;padding-left:18px;color:var(--green);font-weight:900}
.price .num{font-size:64px;line-height:1}
.price .unit{font-size:13px;line-height:1.2;margin:0 4px}
.price .yen{font-size:40px}
.price .fee{font-size:32px;margin-left:4px}

.lead{left:28px;top:228px;font-size:17px;font-weight:700;color:var(--green-dark)}
.lead-copy{left:400px;top:218px;width:420px;font-size:10px;line-height:1.5}

.sports{left:28px;top:268px;width:795px;height:72px;background:linear-gradient(90deg,var(--yellow-band),#f0e78a);border-radius:6px}

.points{left:28px;top:352px;width:795px;display:grid;grid-template-columns:1fr 1fr;gap:10px 14px}
.point{background:var(--green);color:var(--white);font-size:23px;font-weight:800;height:40px;border-radius:20px;display:flex;align-items:center;padding-left:34px;position:relative}
.point::before{content:"";position:absolute;left:12px;width:14px;height:14px;border-radius:50%;background:var(--yellow-bg)}

.voice{left:34px;top:460px;width:390px;height:150px;background:var(--note);transform:rotate(-2deg);padding:14px 18px}
.voice-label{font-size:14px;font-weight:700;color:var(--white);background:var(--green);display:inline-block;padding:1px 10px;border-radius:10px}
.voice-school{font-size:20px;font-weight:700;margin-top:8px;color:var(--ink)}
.voice-text{font-size:11px;line-height:1.6;margin-top:6px}
.team-photo{left:450px;top:460px;width:373px;height:160px;background:linear-gradient(135deg,#8f7a62,var(--photo));}

.cut{left:0;top:660px;width:851px;border-top:2px dashed var(--green)}
.fax-head{left:0;top:672px;width:851px;text-align:center;font-size:20px;font-weight:700}

.order{left:28px;top:706px;width:795px;height:420px;background:var(--white);border:2px solid var(--line)}
.customer{left:0;top:0;width:520px}
.row{display:flex;border-bottom:1px solid var(--line)}
.row .label{width:90px;font-size:13px;padding:8px;border-right:1px solid var(--line)}
.row .field{flex:1;font-size:13px;padding:8px}
.delivery{left:540px;top:0;width:253px;height:230px;border-left:1px solid var(--line)}
.delivery h3{font-size:13px;padding:6px 10px;border-bottom:1px solid var(--line)}
.date-row{display:flex;height:190px}
.date{flex:1;display:flex;align-items:center;justify-content:space-around;font-size:16px;border-right:1px solid var(--line)}
.times{width:120px;display:flex;flex-direction:column;justify-content:space-around;padding:10px;font-size:12px}
.times span::before{content:"";display:inline-block;width:10px;height:10px;border:1px solid var(--ink);margin-right:6px;vertical-align:-1px}
.product{left:0;top:268px;width:791px;height:148px;border-top:1px solid var(--line);display:flex;align-items:center}
.product-img{width:140px;height:120px;margin:0 14px;background:linear-gradient(135deg,#f5e36a,#c9d86a)}
.product-name{font-size:15px;font-weight:700;width:180px}
.product-price{font-size:13px}
.product-price b{font-size:34px;font-weight:900}
.qty{margin-left:auto;margin-right:40px;width:150px;border-bottom:1px solid var(--ink);text-align:right;font-size:15px;padding-bottom:4px}

.footer{left:28px;top:1158px;width:795px;font-size:10px;display:flex;justify-content:space-between}
</style>
</head>
<body>
<main class="flyer">
  <p class="abs tagline rounded"><span class="dot"></span>老舗のバナナ問屋「青葉(あおば)」</p>
  <h1 class="abs title rounded">バナナの宅配サービス</h1>
  <div class="abs delivery-icon" role="img" aria-label="荷物を運ぶ配達員のイラスト"></div>

  <section class="abs price-band">
    <div class="origin">
      <p class="origin-name rounded">エクアドル産<br>バナナ</p>
      <p class="brand rounded"><span class="sq"></span>SOLEA</p>
    </div>
    <div class="price rounded">
      <span class="num">2500</span><span class="unit">(税別)<br>1ケース</span><span class="yen">円</span><span class="fee">＋ 送料</span>
    </div>
  </section>

  <p class="abs lead">味にこだわれば、エクアドル産</p>
  <p class="abs lead-copy">標高の高い農園で時間をかけて育ったバナナは、甘みと香りが豊か。練習の合間の栄養補給に最適です。ご注文いただいたバナナは飛燕パックで部室まで直接お届けします。</p>

  <div class="abs sports" role="img" aria-label="様々なスポーツをする選手のシルエットイラスト"></div>

  <ul class="abs points rounded" style="list-style:none">
    <li class="point">選手の充電　2時間→3時間</li>
    <li class="point">頭脳プレー成功率 120％ UP</li>
    <li class="point">いつでも気軽にぐいっと</li>
    <li class="point">軽くて持ちやすいフォルム</li>
  </ul>

  <article class="abs voice">
    <span class="voice-label">voice</span>
    <p class="voice-school">○○大学　○○○○部</p>
    <p class="voice-text">練習前にみんなで食べています。腹持ちが良く、最後まで集中力が続くようになりました。届くのが毎週の楽しみです。</p>
  </article>
  <div class="abs team-photo" role="img" aria-label="バナナを持つ大学運動部員の集合写真"></div>

  <div class="abs cut"></div>
  <h2 class="abs fax-head">【FAX ご注文用紙　FAX 番号：03-0000-0000】</h2>

  <section class="abs order">
    <div class="abs customer">
      <div class="row"><span class="label">お名前<br><small>(フリガナ)</small></span><span class="field"></span></div>
      <div class="row" style="height:80px"><span class="label">ご住所</span><span class="field">〒</span></div>
      <div class="row"><span class="label">TEL</span><span class="field"></span></div>
      <div class="row"><span class="label">FAX</span><span class="field"></span></div>
    </div>
    <div class="abs delivery">
      <h3>お届け日</h3>
      <div class="date-row">
        <div class="date"><span>月</span><span>日</span></div>
        <div class="times"><span>午前中</span><span>12〜14時</span><span>14〜16時</span><span>16〜18時</span><span>18〜20時</span></div>
      </div>
    </div>
    <div class="abs product">
      <div class="product-img" role="img" aria-label="エクアドル産バナナのケース写真"></div>
      <p class="product-name">エクアドル産バナナ</p>
      <p class="product-price">(1ケース) <b>2500</b>円(税別)</p>
      <p class="qty">ケース</p>
    </div>
  </section>

  <footer class="abs footer">
    <span>株式会社 青葉　東京都港区青葉台1丁目2番3号</span>
    <span>TEL：03-1234-5678　FAX：03-1234-5679　www.aobafruits.example</span>
  </footer>
</main>
</body>
</html>
```